R.T. Framecraft Postcard Design

We need a postcard designed around the utility rebates for window installations. For customers who have Electric heated homes can receive $6 per square foot for each window and patio door and for Natural gas heated homes, they can get $75.00 per window and patio door. The $6 per square foot for electric heated customers is the better rebate averaging about $1000.00 for a house with 10 windows and a patio door. Our Company colors are maroon, black and white, we would like to have a post card designed around these colors. The postcard should be designed to share about these 2 rebates and having a window installation theme. You can use pictures off of our website...www.rtframecraft.example

Target Market(s)

Homeowners with electric heat or Natural gas heat

Industry/Entity Type

Utility

Requirements
Must have
• Blank white square on the back for me to hand write address information.

```html
<!DOCTYPE html>
<html lang="en">
<head>
<meta charset="utf-8">
<title>R.T. Framecraft Postcard</title>
<link rel="stylesheet" href="https://fonts.googleapis.com/css2?family=Archivo+Black&family=Oswald:wght@500;600&family=Source+Sans+3:wght@400;600&display=swap">
<style>
  :root {
    --maroon: #8a0a0c;
    --red: #c8252b;
    --black: #231f20;
    --white: #ffffff;
    --grey: #c9c9c9;
    --ink: #2b2b2b;
    --faint: #e4e4e4;
    --page: #efece8;
  }
  * { box-sizing: border-box; margin: 0; padding: 0; }
  html, body { width: 849px; height: 1200px; overflow: hidden; background: var(--page); }
  body { position: relative; font-family: "Source Sans 3", sans-serif; }

  .card { position: absolute; left: 22px; width: 783px; overflow: hidden; }
  .front { top: 18px; height: 555px; background: var(--black); }
  .back { top: 598px; height: 550px; background: var(--white); }

  .front-bg { position: absolute; inset: 0; }

  .brand-mark { position: absolute; left: 33px; top: 29px; width: 185px; height: 123px;
    display: flex; flex-direction: column; align-items: center; justify-content: center; gap: 10px; }
  .brand-square { width: 58px; height: 58px; background: var(--white); }
  .brand-mark .brand-name { font-family: "Oswald", sans-serif; font-weight: 600; font-size: 22px;
    color: var(--white); letter-spacing: 1px; white-space: nowrap; }

  .headline { position: absolute; left: 240px; top: 38px; width: 517px; text-align: right; white-space: nowrap;
    font-family: "Archivo Black", sans-serif; font-size: 44px; line-height: 1; color: var(--white); }
  .tagline { position: absolute; left: 240px; top: 100px; width: 517px; text-align: right; white-space: nowrap;
    font-family: "Oswald", sans-serif; font-weight: 600; font-size: 17.5px; letter-spacing: 0.6px; color: var(--white); }

  .photo { position: absolute; border: 2px solid var(--white); }
  .photo-1 { left: 26px; top: 167px; width: 177px; height: 105px; background: linear-gradient(135deg, #dcd6c4, #7b8a5a); }
  .photo-2 { left: 96px; top: 242px; width: 175px; height: 105px; background: linear-gradient(135deg, #f2f2ef, #b9bcb0); }
  .photo-3 { left: 26px; top: 317px; width: 177px; height: 105px; background: linear-gradient(135deg, #e8e6df, #8e9a7c); }
  .photo-4 { left: 96px; top: 392px; width: 175px; height: 102px; background: linear-gradient(135deg, #c9a782, #6c5a43); }

  .rebate { position: absolute; left: 290px; width: 462px; display: flex; align-items: center; }
  .rebate-amount { flex: none; width: 118px; height: 118px; border-radius: 50%;
    background: var(--maroon); border: 3px solid #111; display: flex; align-items: center; justify-content: center;
    font-family: "Archivo Black", sans-serif; font-size: 46px; color: var(--white); }
  .rebate-text { margin-left: 18px; font-size: 17.5px; line-height: 1.3; letter-spacing: 0.6px;
    color: var(--white); text-align: justify; }
  .rebate-1 { top: 140px; }
  .rebate-2 { top: 261px; }
  .rebate-3 { top: 378px; }

  .front-band { position: absolute; left: 0; right: 0; top: 500px; height: 34px; background: var(--maroon);
    font-family: "Oswald", sans-serif; font-weight: 600; font-size: 23px; letter-spacing: 0.8px;
    color: var(--white); display: flex; align-items: center; justify-content: center; white-space: nowrap; }

  .back-panel { position: absolute; left: 0; top: 0; width: 344px; height: 457px; }
  .back-bg { position: absolute; inset: 0; }
  .back-brand { position: absolute; left: 62px; top: 24px; width: 220px; height: 170px;
    display: flex; flex-direction: column; align-items: center; justify-content: flex-end; gap: 16px; }
  .back-brand .brand-square { width: 80px; height: 80px; background: var(--maroon); }
  .back-brand .brand-name { font-family: "Oswald", sans-serif; font-weight: 600; font-size: 28px; color: var(--ink); white-space: nowrap; }
  .back-label { position: absolute; left: 0; top: 210px; width: 346px; height: 74px; background: var(--maroon);
    box-shadow: 2px 3px 5px rgba(0,0,0,0.4); display: flex; align-items: center; justify-content: center;
    text-align: center; font-family: "Oswald", sans-serif; font-weight: 600; font-size: 17px; line-height: 1.3;
    color: var(--white); }
  .contacts { position: absolute; left: 58px; top: 316px; list-style: none; color: var(--white); font-size: 19px; }
  .contacts li { display: flex; align-items: center; height: 31px; white-space: nowrap; }
  .contacts svg { width: 16px; height: 16px; margin-right: 12px; fill: none; stroke: var(--white); stroke-width: 1.4; }

  .address { position: absolute; left: 356px; top: 52px; width: 166px; font-size: 16px; line-height: 1.45;
    color: var(--ink); text-align: right; font-style: normal; white-space: nowrap; }

  .back-footer { position: absolute; left: 38px; top: 470px; display: flex; align-items: center; gap: 18px; }
  .back-footer .brand-square { width: 64px; height: 64px; background: var(--faint); }
  .back-footer .brand-name { font-family: "Archivo Black", sans-serif; font-size: 58px; color: var(--faint); white-space: nowrap; }
</style>
</head>
<body>

<section class="card front">
  <svg class="front-bg" width="783" height="555" viewBox="0 0 783 555">
    <defs>
      <linearGradient id="redFade" x1="0" y1="0" x2="1" y2="0">
        <stop offset="0" stop-color="#b81f25"/>
        <stop offset="1" stop-color="#d02a30"/>
      </linearGradient>
    </defs>
    <rect width="783" height="555" fill="#231f20"/>
    <path d="M0 0 H240 C120 80 30 180 28 300 C28 420 130 500 240 555 H0 Z" fill="url(#redFade)"/>
  </svg>

  <div class="brand-mark">
    <div class="brand-square"></div>
    <span class="brand-name">R.T. FRAMECRAFT</span>
  </div>

  <h1 class="headline">R.T. FRAMECRAFT</h1>
  <p class="tagline">YOUR LEADER IN QUALITY WINDOW INSTALLATIONS</p>

  <div class="photo photo-1" role="img" aria-label="Bright living room with large windows and a green sofa"></div>
  <div class="photo photo-2" role="img" aria-label="Homeowner standing beside new white windows"></div>
  <div class="photo photo-3" role="img" aria-label="Corner of a room lined with white framed windows"></div>
  <div class="photo photo-4" role="img" aria-label="Cosy lounge with a wide bank of windows"></div>

  <div class="rebate rebate-1">
    <div class="rebate-amount">$6</div>
    <p class="rebate-text">For customers who have Electric heated homes can receive $6 per square foot for each window</p>
  </div>
  <div class="rebate rebate-2">
    <div class="rebate-amount">$75</div>
    <p class="rebate-text">Patio door and for Natural gas heated homes, they can get $75.00 per window and patio door.</p>
  </div>
  <div class="rebate rebate-3">
    <div class="rebate-amount">$6</div>
    <p class="rebate-text">The $6 per square foot for electric heated customers is the better rebate averaging about $1000.00 for a house with 10 windows and a patio door.</p>
  </div>

  <div class="front-band">INSTALLING WINDOWS THE RIGHT WAY EVERY TIME SINCE 1985</div>
</section>

<section class="card back">
  <div class="back-panel">
    <svg class="back-bg" width="344" height="457" viewBox="0 0 344 457">
      <rect width="344" height="457" fill="#c9c9c9"/>
      <path d="M344 122 L0 335 V457 H344 Z" fill="#8a0a0c"/>
    </svg>

    <div class="back-brand">
      <div class="brand-square"></div>
      <span class="brand-name">R.T. FRAMECRAFT</span>
    </div>

    <div class="back-label">INSTALLING WINDOWS<br>THE RIGHT WAY<br>EVERY TIME SINCE 1985</div>

    <ul class="contacts">
      <li><svg viewBox="0 0 16 16"><rect x="1.5" y="3.5" width="13" height="9"/><path d="M1.5 3.5 L8 9 L14.5 3.5"/></svg>admin@rtframecraft.example</li>
      <li><svg viewBox="0 0 16 16"><path d="M2 6 Q8 1 14 6 L12.5 8 L10.5 6.5 V5.5 H5.5 V6.5 L3.5 8 Z"/><rect x="4" y="9" width="8" height="5"/></svg>360-555-0147</li>
      <li><svg viewBox="0 0 16 16"><rect x="5" y="1.5" width="6" height="13" rx="1" transform="rotate(-25 8 8)"/></svg>425-555-0182</li>
      <li><svg viewBox="0 0 16 16"><circle cx="8" cy="8" r="6.5"/><ellipse cx="8" cy="8" rx="3" ry="6.5"/><path d="M1.5 8 H14.5"/></svg>www.rtframecraft.example</li>
    </ul>
  </div>

  <address class="address">1207 Cedar Lane NE,<br>Lakeview, Washington<br>98000, United States</address>

  <div class="back-footer">
    <div class="brand-square"></div>
    <span class="brand-name">R.T. FRAMECRAFT</span>
  </div>
</section>

</body>
</html>
```